Newly established winery needs label for its bottles

The Corvelle-Marsan Winery, is a small family owned winery that has been producing wine for little over 3 years. We are now ready to officially start commercializing our products. To do so we are looking for a label for our wine bottles. We are looking for a creative design that will differentiate our bottles from the more conventional labels. We are looking for one label design with 3 color schemes so that we can have a standard look and feel for all three of our wines, while having some differentiation between them with the different color schemes. In summary we are looking for a label that will standout by its uniqueness, simplicity and its modern touch. The label should also reflect the historical significance of the name of the winery. The attached documents offers more detail about the winery, what we are looking for, as well as some technical specification for the label. This label project is also related to a logo project see brief: http://www.pitchgallery.example/project-progress.aspx?briefId=553184). The logo project is now complete and the winning design source files were added to the documents in this brief. Also, details around the information that will need to appear on the label was added to the document list.
Updates
This label project will be on hold temporarily while the logo project is in progress. If you are interested in participating in the logo project, please follow this link: http://www.pitchgallery.example/project-progress.aspx?briefId=553184 Added Wednesday, December 17, 2014
Reason: Deadline extended to give sufficent time for submission and modification to the designs provided.

```html
<!DOCTYPE html>
<html lang="en">
<head>
<meta charset="utf-8">
<title>Corvelle-Marsan Red Wine Label</title>
<link rel="stylesheet" href="https://fonts.googleapis.com/css2?family=Marcellus&family=EB+Garamond:ital@1&display=swap">
<style>
  :root {
    --backdrop: #5f5f5f;
    --label-red: #6a1c1e;
    --label-red-deep: #5a1618;
    --gold: #d8a862;
    --gold-light: #f0cf8e;
    --gold-dark: #a9733a;
    --vine-green: #8a9a3c;
  }
  * { margin: 0; padding: 0; box-sizing: border-box; }
  html, body {
    width: 746px; height: 1200px; overflow: hidden;
    background: var(--backdrop);
  }
  .canvas { position: relative; width: 746px; height: 1200px; }
  .wine-label {
    position: absolute; left: 97px; top: 251px;
    width: 306px; height: 388px;
    transform: scale(1.8); transform-origin: top left;
    background: radial-gradient(ellipse at 50% 40%, var(--label-red) 0%, var(--label-red-deep) 100%);
    color: var(--gold);
    font-family: "Marcellus", serif;
  }
  .frame-outer, .frame-inner { position: absolute; border: 1px solid var(--gold); }
  .frame-outer { inset: 4px; }
  .frame-inner { inset: 8px; border-width: 0.6px; }
  .brand-row {
    position: absolute; top: 35px; left: 0; right: 0;
    display: flex; justify-content: center; align-items: center; gap: 12px;
    font-size: 14.5px; letter-spacing: 0.5px;
  }
  .brand-mark {
    width: 38px; height: 38px; border-radius: 50%;
    border: 1.5px solid var(--gold);
  }
  .grape-motif {
    position: absolute; left: 146px; top: 90px; width: 14px; height: 20px;
    border-radius: 40% 40% 50% 50%;
    background: linear-gradient(180deg, var(--vine-green) 0 30%, #e8e4da 30% 100%);
  }
  .divider { position: absolute; left: 80px; top: 125px; width: 146px; height: 3px; }
  .wine-name {
    position: absolute; top: 140px; left: 0; right: 0; text-align: center;
    font-size: 22px; letter-spacing: 0.5px;
    color: var(--gold-light);
  }
  .origin {
    position: absolute; top: 176px; left: 0; right: 0; text-align: center;
    font-size: 10.5px; letter-spacing: 0.2px;
  }
  .winery-line {
    position: absolute; top: 209px; left: 0; right: 0; text-align: center;
    font-family: "EB Garamond", serif; font-style: italic; font-size: 10.5px;
  }
  .volume, .alcohol {
    position: absolute; top: 279px;
    font-family: "EB Garamond", serif; font-style: italic; font-size: 10px;
    color: var(--gold-light);
  }
  .volume { left: 26px; }
  .alcohol { right: 29px; }
  .vineyard-hills {
    position: absolute; left: 12px; right: 12px; bottom: 9px; height: 92px;
    background: linear-gradient(180deg, rgba(216,168,98,0) 0%, rgba(216,168,98,0.35) 45%, rgba(216,168,98,0.55) 100%);
    clip-path: ellipse(90% 100% at 60% 100%);
  }
</style>
</head>
<body>
<main class="canvas">
  <section class="wine-label">
    <div class="frame-outer"></div>
    <div class="frame-inner"></div>

    <div class="brand-row">
      <span class="brand-name">CORVELLE</span>
      <span class="brand-mark"></span>
      <span class="brand-name">MARSAN</span>
    </div>

    <div class="grape-motif" role="img" aria-label="Small grape cluster with vine leaf"></div>

    <svg class="divider" viewBox="0 0 146 3" aria-hidden="true">
      <defs>
        <linearGradient id="rule" x1="0" x2="1">
          <stop offset="0" stop-color="#d8a862" stop-opacity="0"/>
          <stop offset="0.5" stop-color="#f0cf8e"/>
          <stop offset="1" stop-color="#d8a862" stop-opacity="0"/>
        </linearGradient>
      </defs>
      <rect x="0" y="1" width="146" height="0.8" fill="url(#rule)"/>
      <rect x="62" y="0" width="22" height="2.6" fill="#d8a862"/>
    </svg>

    <h1 class="wine-name">RED WINE</h1>
    <p class="origin">PRODUCT OF QUÉBEC / PRODUIT DU QUÉBEC</p>
    <p class="winery-line">Winery Corvelle-Marsan / Vignoble Corvelle-Marsan</p>

    <p class="volume">750 ml</p>
    <p class="alcohol">11.6% alc./Vol</p>

    <div class="vineyard-hills" role="img" aria-label="Gold line pattern of rolling vineyard hills"></div>
  </section>
</main>
</body>
</html>
```